Bref créative
Stationery
Health centre
Bright & Fun-filled
Meadowlark Wellness Studio
We need cards for different individuals - easily editable
12B Harlow Terrace
Edinburgh
EH4 7QN
info@meadowlarkwellstudio.co.uk
www.meadowlarkwellstudio.co.uk
appointments date and time & cancelation policy.
We require 24 hours cancellation for appointments otherwise a charge may be incurred.

```html
<!DOCTYPE html>
<html lang="en">
<head>
<meta charset="utf-8">
<title>Meadowlark Wellness Studio – Stationery</title>
<link rel="stylesheet" href="https://fonts.googleapis.com/css2?family=Cinzel:wght@500&family=Cormorant+Garamond:wght@500&display=swap">
<style>
  :root {
    --backdrop: #ebebeb;
    --paper: #ffffff;
    --brand-green: #3d7a2c;
    --leaf-green: #6aa83a;
    --sky-blue: #4ea3d9;
    --text-green: #4a7f3a;
    --rule-grey: #b9c6b0;
    --shadow: rgba(0,0,0,0.18);
  }
  * { box-sizing: border-box; margin: 0; padding: 0; }
  html, body { width: 1200px; height: 859px; overflow: hidden; }
  body {
    background: var(--backdrop);
    position: relative;
    font-family: "Cormorant Garamond", Georgia, serif;
    color: var(--text-green);
  }
  .sheet {
    position: absolute;
    background: var(--paper);
    box-shadow: 0 1px 4px var(--shadow);
  }

  /* brand block */
  .brand {
    position: absolute;
    left: 0; right: 0;
    display: flex;
    flex-direction: column;
    align-items: center;
    gap: var(--gap, 4px);
  }
  .brand__dot {
    width: var(--dot, 14px);
    height: var(--dot, 14px);
    border-radius: 50%;
    background: var(--leaf-green);
  }
  .brand__name {
    font-family: "Cinzel", "Times New Roman", serif;
    font-weight: 500;
    font-size: var(--size, 16px);
    color: var(--brand-green);
    letter-spacing: 0.04em;
    white-space: nowrap;
  }
  .swoosh {
    position: absolute;
    height: 2px;
    background: linear-gradient(90deg, rgba(78,163,217,0) 0%, var(--sky-blue) 50%, rgba(78,163,217,0) 100%);
  }

  .contact {
    position: absolute;
    left: 0; right: 0;
    text-align: center;
    font-size: var(--csize, 8px);
    line-height: 1.45;
    color: var(--text-green);
  }

  /* letterhead */
  .letterhead { left: 48px; top: 29px; width: 511px; height: 749px; }
  .letterhead .brand { top: 18px; --size: 17px; --dot: 18px; --gap: 6px; }
  .letterhead .swoosh { left: 14px; right: 14px; top: 72px; }
  .letterhead .contact { bottom: 16px; --csize: 8.5px; }

  /* business card */
  .business-card { left: 600px; top: 29px; width: 214px; height: 134px; }
  .business-card .brand { top: 14px; --size: 9px; --dot: 10px; --gap: 3px; }
  .business-card .swoosh { left: 10px; right: 10px; top: 46px; height: 1.5px; }
  .business-card .contact { bottom: 14px; --csize: 6px; }

  /* appointment card */
  .appointment-card { left: 828px; top: 29px; width: 209px; height: 134px; }
  .appointment-card .brand { top: 10px; --size: 7px; --dot: 7px; --gap: 2px; }
  .appointment-fields {
    position: absolute; left: 14px; right: 14px; top: 34px;
    font-size: 7px; line-height: 12px;
  }
  .appointment-fields .field { display: flex; gap: 4px; }
  .appointment-fields .field span:last-child {
    flex: 1; border-bottom: 1px dotted var(--rule-grey); margin-bottom: 3px;
  }
  .appointment-policy {
    position: absolute; left: 12px; right: 12px; bottom: 14px;
    text-align: center; font-size: 6.2px; line-height: 1.4;
  }

  /* compliments slip */
  .compliments-slip { left: 600px; top: 187px; width: 559px; height: 293px; }
  .compliments-slip .brand { top: 22px; --size: 16px; --dot: 16px; --gap: 5px; }
  .compliments-slip .swoosh { left: 14px; right: 14px; top: 70px; }
  .compliments-slip .contact { bottom: 18px; --csize: 7.5px; }

  /* envelope */
  .envelope { left: 600px; top: 523px; width: 559px; height: 293px; }
  .envelope .flap { position: absolute; left: 0; top: 0; width: 100%; height: 90px; }
  .envelope .brand { left: 40px; right: auto; top: 50px; --size: 13px; --dot: 13px; --gap: 4px; }
</style>
</head>
<body>

  <section class="sheet letterhead" aria-label="Letterhead">
    <div class="brand"><span class="brand__dot"></span><span class="brand__name">Meadowlark Wellness Studio</span></div>
    <div class="swoosh"></div>
    <address class="contact" style="font-style:normal">
      12B Harlow Terrace, Edinburgh EH4 7QN<br>
      Phone: 0131 496 0732 &nbsp;•&nbsp; Email: info@meadowlarkwellstudio.co.uk<br>
      www.meadowlarkwellstudio.co.uk
    </address>
  </section>

  <section class="sheet business-card" aria-label="Business card front">
    <div class="brand"><span class="brand__dot"></span><span class="brand__name">Meadowlark Wellness Studio</span></div>
    <div class="swoosh"></div>
    <address class="contact" style="font-style:normal">
      12B Harlow Terrace, Edinburgh EH4 7QN<br>
      Phone: 0131 496 0732 &nbsp;•&nbsp; Email: info@meadowlarkwellstudio.co.uk<br>
      www.meadowlarkwellstudio.co.uk
    </address>
  </section>

  <section class="sheet appointment-card" aria-label="Appointment card back">
    <div class="brand"><span class="brand__dot"></span><span class="brand__name">Appointment</span></div>
    <div class="appointment-fields">
      <div class="field"><span>Name:</span><span></span></div>
      <div class="field"><span>Date:</span><span></span></div>
      <div class="field"><span>Time:</span><span></span></div>
    </div>
    <p class="appointment-policy">
      We require 24 hours cancellation for appointments<br>
      otherwise a charge may be incurred.<br>
      Thank you for choosing our studio.
    </p>
  </section>

  <section class="sheet compliments-slip" aria-label="Compliments slip">
    <div class="brand"><span class="brand__dot"></span><span class="brand__name">Meadowlark Wellness Studio</span></div>
    <div class="swoosh"></div>
    <address class="contact" style="font-style:normal">
      12B Harlow Terrace, Edinburgh EH4 7QN<br>
      Phone: 0131 496 0732 &nbsp;•&nbsp; Email: info@meadowlarkwellstudio.co.uk<br>
      www.meadowlarkwellstudio.co.uk
    </address>
  </section>

  <section class="sheet envelope" aria-label="Envelope">
    <svg class="flap" viewBox="0 0 559 90" preserveAspectRatio="none" aria-hidden="true">
      <polyline points="0,0 279.5,88 559,0" fill="none" stroke="#e4e4e4" stroke-width="1.2"/>
    </svg>
    <div class="brand"><span class="brand__dot"></span><span class="brand__name">Meadowlark Wellness Studio</span></div>
  </section>

</body>
</html>
```